LineUp Banner for EDM music Festival!

Hello,

i need a lineup banner for an edm festival.

It should looks similar to the lineup banner uploaded here. I also added the background image.

Feel free to add something you think it looks cool.
Background have to be used. I would need after your work is done the psd file, so I can edit the text / names by myself.

Size should be around 2000x3000.

Thank you

Industry/Entity Type

Festival

Requirements
Must have
• Similar to the lineup banner. Feel free to add something you think it looks cool.
• Background have to be used.
Nice to have
• In best case it will be as most similar as the uploaded lineup banner.

```html
<!DOCTYPE html>
<html lang="en">
<head>
<meta charset="utf-8">
<title>AAA Festival Lineup</title>
<link rel="stylesheet" href="https://fonts.googleapis.com/css2?family=Archivo+Black&family=Oswald:wght@500;600&family=Roboto:wght@500&display=swap">
<style>
  :root {
    --night: #06080f;
    --deep-blue: #0f2a66;
    --haze-yellow: #f3e79a;
    --amber: #c8731c;
    --ember: #7a2a0c;
    --shadow-brown: #1a0d05;
    --present-blue: #1d6aa3;
    --gold-light: #fff3c4;
    --gold-mid: #f0b54a;
    --gold-dark: #9a5610;
    --text-white: #ffffff;
    --info-grey: #dcdcdc;
  }
  * { margin: 0; padding: 0; box-sizing: border-box; }
  html, body { width: 800px; height: 1200px; overflow: hidden; background: var(--night); }
  .poster { position: relative; width: 800px; height: 1200px; overflow: hidden; }

  .backdrop {
    position: absolute; inset: 0;
    background:
      radial-gradient(ellipse 60% 22% at 50% 46%, rgba(243,231,154,0.85), transparent 70%),
      radial-gradient(ellipse 40% 30% at 100% 20%, rgba(122,42,12,0.8), transparent 70%),
      radial-gradient(ellipse 50% 25% at 5% 38%, rgba(15,42,102,0.9), transparent 70%),
      linear-gradient(180deg, var(--night) 0%, #0b1530 25%, var(--deep-blue) 38%, var(--haze-yellow) 52%, var(--amber) 64%, var(--ember) 80%, var(--shadow-brown) 100%);
  }

  .presenter {
    position: absolute; top: 30px; left: 0; width: 100%;
    text-align: center;
    font-family: "Roboto", sans-serif; font-weight: 500;
    font-size: 22px; letter-spacing: 7px;
    color: var(--present-blue);
  }

  .glow {
    position: absolute; left: 150px; width: 500px; height: 6px;
    background: radial-gradient(ellipse at center, #fff2c0 0%, #ff9a2a 35%, rgba(255,110,20,0) 75%);
    filter: blur(1px);
  }
  .glow--top { top: 92px; }
  .glow--bottom { top: 230px; }

  .gold {
    background: linear-gradient(180deg, var(--gold-light) 0%, var(--gold-mid) 45%, var(--gold-dark) 80%, var(--gold-mid) 100%);
    -webkit-background-clip: text; background-clip: text;
    color: transparent;
  }

  .festival-title {
    position: absolute; top: 104px; left: 0; width: 100%;
    text-align: center; white-space: nowrap;
    font-family: "Archivo Black", sans-serif;
    font-size: 92px; line-height: 120px;
    letter-spacing: -1px;
    transform: scale(0.85, 1.3);
    transform-origin: 50% 50%;
  }

  .event-date {
    position: absolute; top: 262px; left: 0; width: 100%;
    text-align: center; white-space: nowrap;
    font-family: "Oswald", sans-serif; font-weight: 600;
    font-size: 54px; line-height: 64px;
  }
  .event-date sup { font-size: 25px; vertical-align: 22px; }

  .lineup {
    position: absolute; top: 378px; left: 40px; width: 740px;
    display: grid; grid-template-columns: 388px auto;
    font-family: "Oswald", sans-serif; font-weight: 500;
    font-size: 52px; line-height: 72px;
    color: var(--text-white);
    white-space: nowrap;
  }

  .info {
    position: absolute; top: 976px; left: 40px; width: 750px;
    display: grid; grid-template-columns: 252px 253px auto;
    grid-auto-rows: 33.6px;
    font-family: "Oswald", sans-serif; font-weight: 500;
    font-size: 23.5px; line-height: 33.6px;
    color: var(--info-grey);
    white-space: nowrap;
  }
  .info-column { display: grid; grid-template-rows: repeat(4, 33.6px); grid-row: 1 / span 4; }
  .info-column--short span:first-child { grid-row: 2; }

  .sponsors {
    position: absolute; top: 1128px; left: 0; width: 100%; height: 20px;
    display: flex; align-items: center; gap: 12px;
  }
  .sponsors-rule { flex: 1; height: 2px; background: var(--info-grey); }
  .sponsors-label {
    font-family: "Oswald", sans-serif; font-weight: 500;
    font-size: 16px; line-height: 20px; color: var(--text-white);
  }
</style>
</head>
<body>
<main class="poster">
  <div class="backdrop" role="img" aria-label="Festival crowd with raised hands under warm stage lights, starry night sky above"></div>

  <p class="presenter">AAA PRESENT</p>
  <div class="glow glow--top"></div>
  <h1 class="festival-title gold">AAA Festival</h1>
  <div class="glow glow--bottom"></div>
  <p class="event-date gold">OCTOBER 31<sup>ST</sup>, SUNDAY</p>

  <section class="lineup">
    <span class="artist">DJ ARTIST NAME</span>
    <span class="artist">DJ ARTIST NAME</span>
    <span class="artist">DJ ARTIST NAME</span>
    <span class="artist">DJ ARTIST NAME</span>
  </section>

  <section class="info">
    <div class="info-column info-column--short">
      <span>GENERAL INFORMATIONS</span>
      <span>GENERAL INFORMATIONS</span>
      <span>GENERAL INFORMATIONS</span>
    </div>
    <div class="info-column">
      <span>GENERAL INFORMATIONS</span>
      <span>GENERAL INFORMATIONS</span>
      <span>GENERAL INFORMATIONS</span>
      <span>GENERAL INFORMATIONS</span>
    </div>
    <div class="info-column info-column--short">
      <span>GENERAL INFORMATIONS</span>
      <span>GENERAL INFORMATIONS</span>
      <span>GENERAL INFORMATIONS</span>
    </div>
  </section>

  <footer class="sponsors">
    <span class="sponsors-rule"></span>
    <span class="sponsors-label">SPONSORS</span>
    <span class="sponsors-rule"></span>
  </footer>
</main>
</body>
</html>
```